Harborline Toma's Chinese/Dim Sum Restaurant Menu

Harborline Toma's is a seafood-asian fusion restaurant featuring dim sum and other classical asian fusion items.

We need a menu design that includes both our food menu and our drink menu.

Food menu: Needs to have space for descriptions of food (please just include a place holder and we will input them later). See attached for food menu items.

Drink menu: Just lists of items with prices. See attached Jade Lantern Menu- please include the same items, but rebrand for Harborline Toma's.

The menus must be able to be printed in a 4.25x11in paper.

We want something modern and contemporary. My boss likes geometrical design aspects and minimalism. So, nothing too ornate. But, it has to be different from the Jade Lantern menus. Colors can be black, red, gold or blue- but it must be able to be tied into our black and red Harborline Toma's logo. Including elements of Chinese culture, especially fishing, is a plus, but not necessary.

We also need this in ai format when we download final copy so we can edit in the future.

UPDATE: Please note, we already have a logo.

Target Market(s)

Upscale family diners

Industry/Entity Type

Chinese Food

Font styles to use
Serif
Sans Serif

Colors
0054AA
0677BA
7BADD7
CADEEF
E8F1F8
0094D4
00A9DD
6FCCEA
C7EBF8
E9F6FB
FFC000
F8CF3A
FAE287
FDF2CF
FEFAEE
EB3D1F
EC4F4E
F09395
F8D3D4
FCEDEE

Requirements
Must have
• Classic, minimalist, elegant

```html
<!DOCTYPE html>
<html lang="en">
<head>
<meta charset="utf-8">
<title>Harborline Toma's — Food & Drink Menu</title>
<link rel="stylesheet" href="https://fonts.googleapis.com/css2?family=Montserrat:wght@400;500;600;700;800;900&display=swap">
<style>
:root{
  --red:#e3261b;
  --ink:#111111;
  --paper:#f1f0ee;
  --stage:#a7a7a7;
  --leaf:#8cbf3f;
  --gold:#f8cf3a;
  --muted:#555555;
}
*{box-sizing:border-box;margin:0;padding:0}
html,body{width:792px;height:1200px;overflow:hidden}
body{background:var(--stage);font-family:"Montserrat",sans-serif;color:var(--ink);position:relative}

.panel{position:absolute;width:220px;height:569px;background:var(--paper);overflow:hidden}
.panel::before,.panel::after{content:"";position:absolute;pointer-events:none}
.panel::before{inset:12px;border:1.2px solid var(--red)}
.panel::after{inset:15px;border:.6px solid var(--red)}
.p1{left:33px;top:20px}.p2{left:286px;top:20px}.p3{left:539px;top:20px}
.p4{left:33px;top:611px}.p5{left:286px;top:611px}.p6{left:539px;top:611px}

.brand{position:absolute;left:0;right:0;top:19px;text-align:center}
.p1 .brand{top:22px}
.brand-dot{display:block;width:13px;height:13px;border-radius:50%;background:var(--red);margin:0 auto 6px}
.brand-name{font-size:7.4px;font-weight:700;letter-spacing:.3px;color:var(--ink)}
.socials{display:flex;justify-content:center;gap:5px;margin-top:5px}
.socials span{width:6px;height:6px;border-radius:50%;background:var(--ink)}
.socials span:last-child{background:#bbb}

.band{position:absolute;left:14px;right:15px;background:var(--ink);color:#fff;text-align:center;font-weight:800;letter-spacing:.4px}
.title-big{position:absolute;left:0;right:0;top:113px;text-align:center;color:var(--red);font-size:47px;font-weight:900;letter-spacing:-1px;line-height:1}

.block{position:absolute}
.tag{display:inline-block;background:var(--red);color:#fff;font-size:8px;font-weight:700;padding:1px 9px 1px 8px;line-height:1.25;clip-path:polygon(0 0,100% 0,93% 50%,100% 100%,0 100%,6% 50%);margin-bottom:3px}
.sub{color:var(--red);font-weight:800;font-size:7px;margin:2px 0}

.menu-list{list-style:none}
.menu-list li{display:flex;align-items:center;height:9.3px;font-size:4.3px;font-weight:500;white-space:nowrap}
.p2 .menu-list li{height:8.6px}
.menu-list i{flex:1;border-bottom:.5px dotted #777;margin:0 2px;transform:translateY(1px)}
.menu-list b,.price{background:var(--ink);color:#fff;border-radius:3px;font-size:3.9px;font-weight:700;padding:.6px 2px;min-width:12px;text-align:center;line-height:1}
.caps li{text-transform:uppercase;font-size:3.9px;font-weight:600}
.wide b{min-width:25px}
.mark{display:inline-block;width:3.4px;height:3.4px;border-radius:50%;margin-left:1.2px}
.veg{background:var(--leaf)}.hot{background:var(--red)}.gf{background:var(--gold)}

.photo{position:absolute;border-radius:4px}

.desc-list{list-style:none}
.desc-list li{font-size:3.8px;font-weight:600;text-transform:uppercase;line-height:1.25;margin-bottom:3.2px}
.desc-list .row{display:flex;align-items:center}
.desc-list .row i{flex:1;border-bottom:.5px dotted #777;margin:0 2px}
.desc-list small{display:block;font-size:3.4px;font-weight:400;text-transform:none;color:var(--muted);line-height:1.2}
.desc-list .note{font-size:3.2px;font-weight:500}
.cocktail-list li{margin-bottom:6.6px}

.plain-list{list-style:none;font-size:3.7px;font-weight:700;text-transform:uppercase;line-height:1.23}
.plain-list .flavor{font-weight:500;padding-left:3px}
.plain-list .flavor::before{content:"";display:inline-block;width:2px;height:2px;border-radius:50%;background:var(--red);margin-right:1.5px;vertical-align:middle}
.plain-list .group{margin-top:2px}
.dark-box{position:absolute;background:var(--ink);color:#fff;border-radius:4px;padding:4px 5px}
.dark-box .tag{font-size:6.5px;padding:0 6px}
.dark-box .plain-list{font-size:3.5px}

.happy{position:absolute;left:18px;right:18px;text-align:center}
.happy h3{font-size:7.6px;font-weight:700;line-height:1.25}
.pill{display:inline-block;background:var(--red);color:#fff;font-size:7.6px;font-weight:700;border-radius:6px;padding:1px 12px;margin:3px 0}
.happy p{font-size:5.2px;line-height:1.3}
.fine{font-size:4px;line-height:1.3;text-transform:uppercase}
.rule{height:.5px;background:#999;margin:4px 20px}
</style>
</head>
<body>

<!-- Food cover + dim sum + soup -->
<section class="panel p1">
  <header class="brand"><span class="brand-dot"></span><div class="brand-name">HARBORLINE TOMA'S</div><div class="socials"><span></span><span></span><span></span></div></header>
  <div class="band" style="top:85px;height:28px;font-size:18px;line-height:28px">FOOD &amp; DRINK</div>
  <div class="title-big">MENU</div>
  <div class="photo" role="img" aria-label="Plate of shrimp stir-fried noodles with lime on a red geometric border" style="left:22px;top:172px;width:176px;height:146px;border-radius:50%;background:radial-gradient(circle,#e7a46b 0 30%,#f4f1ec 31% 47%,#e3261b 48% 60%,#f1f0ee 61%)"></div>

  <div class="block" style="left:24px;top:339px;width:120px">
    <div class="tag">DIM SUM</div>
    <ul class="menu-list">
      <li>Potsticker<i></i><b>$12</b></li>
      <li>Plant-Based Dumpling<span class="mark veg"></span><i></i><b>$11</b></li>
      <li>Lobster Dumpling<i></i><b>$13</b></li>
      <li>Sticky Rice<i></i><b>$5</b></li>
      <li>Pork Siu Mai<i></i><b>$12</b></li>
      <li>Spicy Won Ton<span class="mark hot"></span><i></i><b>$12</b></li>
      <li>Vegan Spicy Won Ton<span class="mark veg"></span><span class="mark hot"></span><i></i><b>$12</b></li>
      <li>Pork Xie Long Bao<i></i><b>$11</b></li>
      <li>Crab &amp; Pork Xie Long Bao<i></i><b>$12</b></li>
      <li>BBQ Pork Bao<i></i><b>$10</b></li>
      <li>Sweet Corn Dumpling<span class="mark veg"></span><i></i><b>$11</b></li>
    </ul>
  </div>
  <div class="photo" role="img" aria-label="Dim sum dumplings on a white plate" style="left:155px;top:349px;width:42px;height:103px;background:linear-gradient(#fff,#c77a45 20% 80%,#fff)"></div>

  <div class="block" style="left:76px;top:471px;width:121px">
    <div class="tag">SOUP</div>
    <ul class="menu-list">
      <li>Cup Hot &amp; Sour Soup<span class="mark hot"></span><i></i><b>$5</b></li>
      <li>Bowl Hot &amp; Sour Soup<span class="mark hot"></span><i></i><b>$8</b></li>
      <li>Cup Egg Flower Soup<i></i><b>$5</b></li>
      <li>Bowl Egg Flower Soup<i></i><b>$8</b></li>
      <li>Bowl Pork Wonton Soup<i></i><b>$9</b></li>
    </ul>
  </div>
  <div class="photo" role="img" aria-label="White soup pot with orange soup" style="left:22px;top:489px;width:50px;height:32px;background:radial-gradient(ellipse,#e98a3c 0 35%,#e9e9e9 36%)"></div>
</section>

<!-- Appetizers, sauteed, veggie, rice & noodles, sweets -->
<section class="panel p2">
  <header class="brand"><span class="brand-dot"></span><div class="brand-name">HARBORLINE TOMA'S</div><div class="socials"><span></span><span></span><span></span></div></header>

  <div class="block" style="left:24px;top:70px;width:121px">
    <div class="tag">APPETIZERS</div>
    <ul class="menu-list">
      <li>Walnut Shrimp Warp<span class="mark gf"></span><i></i><b>$12</b></li>
      <li>Chicken Lettuce Warp<i></i><b>$12</b></li>
      <li>Tofu Lettuce Warp<span class="mark veg"></span><i></i><b>$12</b></li>
      <li>Curry Mussels + add Noodles<i></i><b>$15</b></li>
      <li>Seabass Roll<i></i><b>$12</b></li>
      <li>Crab Cheese Wonton<i></i><b>$10</b></li>
      <li>Tuna Tower<i></i><b>$23</b></li>
      <li>Ahi Tuna and Fish Chips<i></i><b>$21</b></li>
      <li>Edamame<span class="mark veg"></span><span class="mark gf"></span><i></i><b>$7</b></li>
      <li>Sesame Soy Noodle Salad (cold)<span class="mark veg"></span><i></i><b>$8</b></li>
      <li>Chinese Pancake<span class="mark veg"></span><i></i><b>$9</b></li>
      <li>Garlic Cucumber Salad<span class="mark veg"></span><i></i><b>$8</b></li>
      <li>29 Seaweed Salad<span class="mark veg"></span><i></i><b>$9</b></li>
    </ul>
  </div>
  <div class="photo" role="img" aria-label="Lettuce wrap in a tall glass" style="left:149px;top:96px;width:50px;height:105px;background:linear-gradient(#6fb33a,#e6dccd 55%,#f1f0ee)"></div>

  <div class="block" style="left:72px;top:214px;width:118px">
    <div class="tag">SAUTEED</div>
    <ul class="menu-list">
      <li>Szechuan Seabass<i></i><b>$12</b></li>
      <li>Seabass Black Bean Sauce<i></i><b>$11</b></li>
      <li>Kung Po Shrimp<span class="mark hot"></span><span class="mark gf"></span><i></i><b>$13</b></li>
      <li>Kung Po Chicken<span class="mark hot"></span><i></i><b>$5</b></li>
      <li>Kung Po Tofu<span class="mark hot"></span><span class="mark veg"></span><span class="mark gf"></span><i></i><b>$12</b></li>
      <li>Broccoli Chicken<i></i><b>$12</b></li>
      <li>Broccoli Beef<i></i><b>$12</b></li>
      <li>Broccoli Shrimp<span class="mark gf"></span><i></i><b>$11</b></li>
      <li>Mongolian Beef<span class="mark hot"></span><i></i><b>$12</b></li>
      <li>General Ng's Chicken<span class="mark hot"></span><i></i><b>$10</b></li>
      <li>General Ng's Tofu<span class="mark hot"></span><span class="mark veg"></span><i></i><b>$11</b></li>
    </ul>
  </div>
  <div class="photo" role="img" aria-label="Three plates of sauteed dishes" style="left:18px;top:232px;width:48px;height:88px;background:linear-gradient(#f4f4f4,#a6412a 20%,#f4f4f4 35%,#6d2a1e 50%,#f4f4f4 65%,#4d6b2e 80%,#f4f4f4)"></div>

  <div class="block" style="left:22px;top:338px;width:123px">
    <div class="tag">VEGGIE</div>
    <ul class="menu-list">
      <li>Sauteed Green Beans<span class="mark veg"></span><span class="mark gf"></span><i></i><b>$5</b></li>
      <li>Iceberg Lettuce with "Oyster" Sauce<span class="mark veg"></span><i></i><b>$8</b></li>
      <li>Broccoli Garlic Sauce<span class="mark veg"></span><span class="mark gf"></span><i></i><b>$5</b></li>
    </ul>
  </div>
  <div class="photo" role="img" aria-label="Bowl of green vegetable puree with broccoli" style="left:154px;top:343px;width:44px;height:28px;background:radial-gradient(circle at 40% 50%,#9aa845 0 40%,#f1f0ee 42%)"></div>

  <div class="block" style="left:72px;top:390px;width:120px">
    <div class="tag">RICE &amp; NOODLES</div>
    <ul class="menu-list">
      <li>Seafood Fried Rice<i></i><b>$12</b></li>
      <li>Veggie Fried Rice<i></i><b>$12</b></li>
      <li>Chicken Fried Rice<i></i><b>$12</b></li>
      <li>Beef Fried Rice<i></i><b>$15</b></li>
      <li>Seafood Chow Mein<i></i><b>$12</b></li>
      <li>Chicken Chow Mein<i></i><b>$10</b></li>
      <li>Beef Chow Mein<i></i><b>$23</b></li>
    </ul>
  </div>
  <div class="photo" role="img" aria-label="Plates of fried rice and chow mein" style="left:18px;top:392px;width:48px;height:70px;background:linear-gradient(#e1c27a,#c7a05a 50%,#d8c7a4)"></div>

  <div class="block" style="left:24px;top:480px;width:121px">
    <div class="tag">SWEET &amp; DESSERT</div>
    <ul class="menu-list">
      <li>Chocolate Dumpling<i></i><b>$5</b></li>
      <li>Sweet Egg Bao<i></i><b>$8</b></li>
      <li>Walnut Bao<i></i><b>$5</b></li>
    </ul>
  </div>
  <div class="photo" role="img" aria-label="Dark sesame dessert balls in a bowl" style="left:150px;top:487px;width:42px;height:26px;background:radial-gradient(ellipse,#2f2a27 0 45%,#c9935b 47% 60%,#f1f0ee 62%)"></div>
</section>

<!-- Drinks cover: desserts, NA beverages, happy hour -->
<section class="panel p3">
  <header class="brand"><span class="brand-dot"></span><div class="brand-name">HARBORLINE TOMA'S</div><div class="socials"><span></span><span></span><span></span></div></header>
  <div class="band" style="top:65px;height:19px;font-size:16px;line-height:19px">DRINKS</div>

  <div class="block" style="left:21px;top:102px;width:122px">
    <div class="tag">DESSERTS</div>
    <ul class="desc-list">
      <li><span class="row">Pure Decadence<i></i><span class="price">$12</span></span><small>Molten Chocolate Lava Cake, Pineapple Coconut Ice Cream, Whipped Cream</small></li>
      <li><span class="row">Cheesecake<i></i><span class="price">$15</span></span></li>
      <li><span class="row">Pineapple Coconut Ice Cream<i></i><span class="price">$15</span></span></li>
      <li><span class="row">Salted Caramel Ice Cream<i></i><span class="price">$15</span></span></li>
      <li><span class="row">Marionberry Sorbet<i></i><span class="price">$15</span></span></li>
      <li><span class="row">Vanilla Ice Cream<i></i><span class="price">$15</span></span></li>
    </ul>
  </div>
  <div class="photo" role="img" aria-label="Berry smoothie in a tall glass" style="left:156px;top:118px;width:31px;height:76px;background:linear-gradient(#f0b9c8,#cf6f91 60%,#efefef)"></div>

  <div class="block" style="left:71px;top:212px;width:119px">
    <div class="tag">NA BEVERAGES</div>
    <ul class="desc-list">
      <li><span class="row">Bottomless – House Cola, Diet Cola, Lemon-Lime Soda, Old Mill Root Beer, Pepper Soda, Ginger Ale, Iced Tea, Lemonade<i></i><span class="price">$12</span></span><span class="note">(NO REFILLS)</span></li>
      <li><span class="row">Apple, Orange, Cranberry, Grapefruit, Pineapple, Chocolate Milk, Milk<i></i><span class="price">$12</span></span><span class="note">(SHAKEN – NO REFILLS)</span></li>
      <li><span class="row">Virgin Pina Colada &amp; Virgin Strawberry Daquiri<i></i><span class="price">$12</span></span><span class="note">(LIMIT ONE REFILL)</span></li>
      <li><span class="row">Strawberry Lemonade, Shirley Temple, Roy Rogers<i></i><span class="price">$12</span></span><span class="note">(LIMIT ONE REFILL)</span></li>
    </ul>
  </div>
  <div class="photo" role="img" aria-label="Pina colada with pineapple garnish" style="left:19px;top:236px;width:44px;height:95px;background:linear-gradient(#f3c33e,#f5ecb2 35%,#f4f0d8 80%,#f1f0ee)"></div>

  <div class="band" style="top:346px;height:19px;font-size:16px;line-height:19px">WESTGATE</div>
  <div class="happy" style="top:386px">
    <h3>HAPPY HOUR APPETIZERS*<br>EVERYDAY</h3>
    <span class="pill">3 PM – 6 PM</span>
    <h3>DRINK &amp; APPETIZERS</h3>
    <p>$5 WELL LIQUORS<br>$1 OFF ALL ALCOHOLIC BEVERAGES</p>
    <div class="rule"></div>
    <p class="fine" style="font-size:5px">*Available only in the bar, dine in only</p>
    <div class="rule"></div>
    <p class="fine">Jade Lantern restaurant reserves the right to change menu selections, and/or the prices that accompany those items, as they appear on the menus at the restaurant. Only one promotion/special/discount/kickback used at a time, per table or check</p>
  </div>
</section>

<!-- Liquor -->
<section class="panel p4">
  <header class="brand"><span class="brand-dot"></span><div class="brand-name">HARBORLINE TOMA'S</div><div class="socials"><span></span><span></span><span></span></div></header>

  <div class="block" style="left:22px;top:73px;width:84px">
    <div class="tag">LIQUOR</div>
    <div class="sub">VODKA</div>
    <ul class="plain-list">
      <li>Nordvik</li><li>Vistula Reserve</li><li>Tidewater Bay</li><li>Silver Heron</li><li>Kiri Vodka</li><li>Kettle Mill</li><li>New Harbor Vodka</li><li>Steppe Gold</li><li>Tall Pines</li><li>Deep Current</li>
      <li class="flavor">Cranberry</li><li class="flavor">Grapefruit</li><li class="flavor">Lemon</li><li class="flavor">Orange</li><li class="flavor">Peach</li><li class="flavor">Sweet Tea</li>
      <li class="group">Summit Peak</li><li class="flavor">Citrus</li>
    </ul>
  </div>
  <div class="photo" role="img" aria-label="Red cocktail glass with berries" style="left:88px;top:160px;width:32px;height:45px;background:linear-gradient(#f1f0ee,#a8152a 30%,#6d0f1c)"></div>

  <div class="dark-box" style="left:126px;top:86px;width:74px;height:47px">
    <div class="tag">GIN</div>
    <ul class="plain-list"><li>Lotus Gin</li><li>Blue Jewel</li><li>Hollow Oak</li><li>Rokka Hill Gin</li><li>Tarn House</li></ul>
  </div>

  <div class="dark-box" style="left:19px;top:213px;width:102px;height:83px;display:flex;gap:6px">
    <div style="flex:1">
      <div class="tag">TEQUILA</div>
      <ul class="plain-list"><li>Casa Nueve Reposada</li><li>Casa Nueve Silver</li><li>Los Cazos</li><li>Hornillo Black Barrel</li><li>Hornillo Plata</li><li>Hornillo Reposada</li><li>Palomar</li><li>Sauceda</li></ul>
    </div>
    <div style="flex:1">
      <div class="tag">RUM</div>
      <ul class="plain-list"><li>Baraco Gold</li><li>Baraco Superior</li><li>Captain Marlow</li><li>Coral Bay 151</li><li>Mayfair's Dark Rum</li><li>Maliha Coconut Rum</li><li>Plantain Pineapple Rum</li></ul>
    </div>
  </div>
  <div class="photo" role="img" aria-label="Row of orange tequila shots with lime" style="left:22px;top:300px;width:96px;height:30px;background:linear-gradient(90deg,#f4a534,#f7c873,#e9772b,#f4a534)"></div>

  <div class="block" style="left:22px;top:341px;width:90px">
    <div class="tag">LIQUORS</div>
    <ul class="plain-list">
      <li>Bailey Cove</li><li>Rosso Amaro</li><li>Highland Honey</li><li>Ember Ball</li><li>Hazel Abbey</li><li>Giraud Pamplemousse</li><li>Giraud Orgeat</li><li>Gold Flake</li><li>Hunter's Herb</li><li>Kaloa</li><li>Green Melon</li><li>Night Roast Coffee</li><li>Peppermint Peak</li><li>Cinder Fire</li><li>Saint Blossom Elderflower</li><li>Isle Cove Distillery</li>
      <li class="flavor">Loganberry</li><li class="flavor">Blackberry</li><li class="flavor">Raspberry</li>
    </ul>
  </div>
  <div class="photo" role="img" aria-label="Dark liquor bottle" style="left:99px;top:410px;width:14px;height:56px;background:linear-gradient(#2b3a3a,#1b2222)"></div>

  <div class="block" style="left:126px;top:140px;width:76px">
    <div class="sub" style="margin-top:0">WHISKEY</div>
    <ul class="plain-list" style="line-height:1.2">
      <li>Copperline Single Blend</li><li>Jacob Dane's</li><li>Seaborne 7</li><li>Bourbon</li>
      <li class="flavor">Basin Hollow</li><li class="flavor">Basin Hollow Red Cask</li><li class="flavor">Bakewell Kentucky Bourbon</li><li class="flavor">Blanford's</li><li class="flavor">Brookers Bourbon</li><li class="flavor">Bison Trail</li><li class="flavor">Cadell Bourbon</li><li class="flavor">Hawk Rare</li><li class="flavor">Harlow Creek</li><li class="flavor">Jay Barrel</li><li class="flavor">Knoll Creek 9</li><li class="flavor">Knoll Creek 12</li><li class="flavor">Maple Mark</li><li class="flavor">Maple Mark Batch Two</li><li class="flavor">Tyler Bourbon</li><li class="flavor">Wellman Special Reserve</li><li class="flavor">Wild Pheasant</li><li class="flavor">Woodbridge Reserve</li>
      <li class="group">Canadian</li><li class="flavor">Black Satin</li><li class="flavor">Crown Regal</li><li class="flavor">MacNeary</li><li class="flavor">Pendle Ridge</li>
      <li class="group">Irish</li><li class="flavor">Tidewater Triple Reserve</li><li class="flavor">Jamison Hill</li><li class="flavor">Redwing</li>
      <li class="group">Japanese</li><li class="flavor">Hibari Blend</li><li class="flavor">Sunwa</li><li class="flavor">Tokiwa</li>
      <li class="group">Rye</li><li class="flavor">Prairie Premium Rye</li><li class="flavor">Cadell Rye</li><li class="flavor">Pendle Ridge Rye</li><li class="flavor">Saxon Rye</li><li class="flavor">Isle Cove Bunker Rye</li>
      <li class="group">Scotch</li><li class="flavor">Balmoral Glen Twin Cask</li><li class="flavor">Clan Macrae</li><li class="flavor">Glenbrook 14</li><li class="flavor">Glenvale 12</li><li class="flavor">Johnny Strider Black</li><li class="flavor">Johnny Strider Red</li>
      <li class="group">Cognac</li><li class="flavor">Courvale</li><li class="flavor">Hennard</li><li class="flavor">Orlan</li>
    </ul>
  </div>

  <div class="block" style="left:22px;top:488px;width:125px">
    <div class="tag">SAKE</div>
    <ul class="menu-list caps">
      <li>Shirotori House Sake<i></i><b>$12</b></li>
      <li>Toryu Winter Veil Nigori<i></i><b>$15</b></li>
      <li>Toryu Winter Veil Nigori<i></i><b>$12</b></li>
      <li>Hikari Citrus Blossom<i></i><b>$15</b></li>
    </ul>
  </div>
  <div class="photo" role="img" aria-label="Red cocktail with cinnamon sticks" style="left:152px;top:497px;width:42px;height:32px;background:linear-gradient(#f1f0ee,#d9352f 40%,#8a3b2a)"></div>
</section>

<!-- Wine & beer -->
<section class="panel p5">
  <header class="brand"><span class="brand-dot"></span><div class="brand-name">HARBORLINE TOMA'S</div><div class="socials"><span></span><span></span><span></span></div></header>
  <div class="photo" role="img" aria-label="Red and white wine bottles with glasses" style="left:144px;top:48px;width:52px;height:44px;background:linear-gradient(90deg,#7a0d18 0 25%,#f1f0ee 25% 50%,#e8dc8e 50% 75%,#f1f0ee 75%)"></div>

  <div class="block" style="left:24px;top:74px;width:173px">
    <div class="tag">WINE</div>
    <div class="sub" style="margin:0 0 1px">BOTTLE ONLY</div>
    <ul class="menu-list caps">
      <li>Tall Shadows Writer's Rise Riesling (WA)<i></i><b>$12</b></li>
      <li>Whitecove Sauvignon Blanc (NZ)<i></i><b>$12</b></li>
      <li>Dunmore Meadow Lane Chardonnay (WA)<i></i><b>$12</b></li>
      <li>Two Vintages Merlot (WA)<i></i><b>$15</b></li>
      <li>Faith Creek Syrah (WA)<i></i><b>$12</b></li>
      <li>Drakehorn Cabernet (WA)<i></i><b>$10</b></li>
      <li>Jorvik Cabernet (CA)<i></i><b>$23</b></li>
      <li>Faith Creek Cabernet (WA)<i></i><b>$21</b></li>
      <li>Abelia Cabernet (WA)<i></i><b>$7</b></li>
      <li>Pepper Ford Cabernet (WA)<i></i><b>$8</b></li>
      <li>Turnback Cabernet (WA)<i></i><b>$9</b></li>
      <li>Lorenti Cabernet (WA)<i></i><b>$8</b></li>
      <li>Mischief Maker Red Blend (CA)<i></i><b>$9</b></li>
      <li>Fidelis Red Blend (WA)<i></i><b>$8</b></li>
      <li>Mathers Chalkline Red (WA)<i></i><b>$9</b></li>
      <li>DeLisle Tier Two Red Blend (WA)<i></i><b>$8</b></li>
      <li>Quill Creek Red Blend (WA)<i></i><b>$9</b></li>
    </ul>
  </div>

  <div class="block" style="left:24px;top:268px;width:173px">
    <div class="tag">WINE</div>
    <ul class="menu-list caps wide">
      <li>Rowan Patrice Riesling<i></i><b>11 / 16 / 40</b></li>
      <li>Tumbler Pinot Gris (OR)<i></i><b>11 / 16 / 40</b></li>
      <li>Brancroft Sauv Blanc (NZ)<i></i><b>11 / 16 / 40</b></li>
      <li>Trancheur Pale Blanc (WA)<i></i><b>11 / 16 / 40</b></li>
      <li>Drakehorn Chardonnay (WA)<i></i><b>11 / 16 / 40</b></li>
      <li>Kendrick Jensen Chardonnay<i></i><b>11 / 16 / 40</b></li>
      <li>Franco Capella Pinot Noir (CA)<i></i><b>11 / 16 / 40</b></li>
      <li>Drumhollow Merlot (WA)<i></i><b>11 / 16 / 40</b></li>
      <li>Four Hooves Merlot (WA)<i></i><b>11 / 16 / 40</b></li>
      <li>Trancheur Cabernet Franc (WA)<i></i><b>11 / 16 / 40</b></li>
      <li>Gander Ridge Syrah (WA)<i></i><b>11 / 16 / 40</b></li>
      <li>Javelin Cabernet (CA)<i></i><b>11 / 16 / 40</b></li>
      <li>Four Hooves Cabernet (WA)<i></i><b>11 / 16 / 40</b></li>
      <li>Tormarina Costa Luce Rose (FR)<i></i><b>11 / 16 / 40</b></li>
      <li>Plum Wine<i></i><b>11 / 16 / 40</b></li>
      <li>Champagne Split<i></i><b>11 / 16 / 40</b></li>
      <li>House White<i></i><b>11 / 16 / 40</b></li>
      <li>House Red<i></i><b>11 / 16 / 40</b></li>
    </ul>
  </div>

  <div class="block" style="left:24px;top:457px;width:173px">
    <div class="tag">BOTTLED BEER</div>
    <div style="display:flex;gap:16px">
      <ul class="menu-list caps" style="flex:1">
        <li>Stellan Cidre<i></i><b>$12</b></li>
        <li>White Crest<i></i><b>$12</b></li>
        <li>Widman Hefeweisen<i></i><b>$12</b></li>
        <li>Blue Harvest<i></i><b>$12</b></li>
        <li>Stellan Abbey<i></i><b>$12</b></li>
        <li>Costa Clara<i></i><b>$12</b></li>
        <li>Gallagher Stout<i></i><b>$12</b></li>
      </ul>
      <ul class="menu-list caps" style="flex:1">
        <li>Heinrik<i></i><b>$12</b></li>
        <li>Qingshan 6<i></i><b>$12</b></li>
        <li>Rainhill 5<i></i><b>$12</b></li>
        <li>Coastal Light 5<i></i><b>$12</b></li>
        <li>Budmore 5<i></i><b>$12</b></li>
        <li>Budmore Light 5<i></i><b>$12</b></li>
        <li>Heinrik 0 6<i></i><b>$12</b></li>
      </ul>
    </div>
  </div>
</section>

<!-- Cocktails -->
<section class="panel p6">
  <header class="brand"><span class="brand-dot"></span><div class="brand-name">HARBORLINE TOMA'S</div><div class="socials"><span></span><span></span><span></span></div></header>
  <div class="photo" role="img" aria-label="Red and white wine bottles with glasses" style="left:144px;top:48px;width:52px;height:44px;background:linear-gradient(90deg,#7a0d18 0 25%,#f1f0ee 25% 50%,#e8dc8e 50% 75%,#f1f0ee 75%)"></div>

  <div class="block" style="left:23px;top:74px;width:174px">
    <div class="tag">COCKTAILS</div>
    <div class="sub" style="margin:0 0 2px">BOTTLE ONLY</div>
    <ul class="desc-list cocktail-list">
      <li><span class="row">Pineapple Daquiri<i></i><span class="price">$12</span></span><small>Plantain Pineapple Rum,<br>Lime Juice, Rich Simple Syrup</small></li>
      <li><span class="row">Elderflower Gimlet<i></i><span class="price">$12</span></span><small>Plantain Pineapple Rum,<br>Lime Juice, Rich Simple Syrup</small></li>
      <li><span class="row">Isle Cove Blackberry Manhattan<i></i><span class="price">$12</span></span><small>Plantain Pineapple Rum,<br>Lime Juice, Rich Simple Syrup</small></li>
      <li><span class="row">Tide &amp; Tonic<i></i><span class="price">$12</span></span><small>Plantain Pineapple Rum,<br>Lime Juice, Rich Simple Syrup</small></li>
      <li><span class="row">Hi-Ya Margarita<i></i><span class="price">$12</span></span><small>Plantain Pineapple Rum,<br>Lime Juice, Rich Simple Syrup</small></li>
      <li><span class="row">Isle Cove Bramble<i></i><span class="price">$12</span></span><small>Plantain Pineapple Rum,<br>Lime Juice, Rich Simple Syrup</small></li>
      <li><span class="row">Rum Punch<i></i><span class="price">$12</span></span><small>Plantain Pineapple Rum,<br>Lime Juice, Rich Simple Syrup</small></li>
      <li><span class="row">Bourbon Lemonade<i></i><span class="price">$12</span></span><small>Plantain Pineapple Rum,<br>Lime Juice, Rich Simple Syrup</small></li>
      <li><span class="row">Tequila Smash<i></i><span class="price">$12</span></span><small>Plantain Pineapple Rum,<br>Lime Juice, Rich Simple Syrup</small></li>
      <li><span class="row">Captain's Goat<i></i><span class="price">$12</span></span><small>Plantain Pineapple Rum,<br>Lime Juice, Rich Simple Syrup</small></li>
      <li><span class="row">Lavender Loganberry Lemon Drop<i></i><span class="price">$12</span></span><small>Plantain Pineapple Rum,<br>Lime Juice, Rich Simple Syrup</small></li>
      <li><span class="row">New Fashioned<i></i><span class="price">$12</span></span><small>Plantain Pineapple Rum,<br>Lime Juice, Rich Simple Syrup</small></li>
      <li><span class="row">Isle Cove Blackberry Manhattan<i></i><span class="price">$12</span></span><small>Plantain Pineapple Rum,<br>Lime Juice, Rich Simple Syrup</small></li>
      <li><span class="row">Hibiscus Margarita<i></i><span class="price">$12</span></span><small>Plantain Pineapple Rum,<br>Lime Juice, Rich Simple Syrup</small></li>
      <li><span class="row">Chinatini<i></i><span class="price">$12</span></span><small>Plantain Pineapple Rum,<br>Lime Juice, Rich Simple Syrup</small></li>
      <li><span class="row">Spirit Free – Summer Sunset<i></i><span class="price">$12</span></span><small>Plantain Pineapple Rum,<br>Lime Juice, Rich Simple Syrup</small></li>
    </ul>
  </div>
  <div class="photo" role="img" aria-label="Row of assorted wine bottles" style="left:35px;top:450px;width:150px;height:98px;background:linear-gradient(90deg,#2b2b2b,#b51d2a 14%,#3b5a2b 28%,#1e1e1e 42%,#d8d49a 56%,#efe9b8 70%,#6e1c2a 85%,#2b2b2b)"></div>
</section>

</body>
</html>
```